New website for a business that provides behaviour analysis

A new website that details the services that are provided around behaviour analysis for people with a disability through QCLP. There also needs to incorporate an about us and a staff page, Plus a referral form that is a google doc.
The business already has a web address that needs to be tailored.
Soft colours are preferred.
Do not have lots of pictures, keep them minimal.
A logo for the business is also needed to be incorporated, and this is a separate project that can be awarded to the website winner.
Website needs to be able to be used on VOB who will be the host for the design.

Target Market(s)

QCLP clients requiring behaviour support clician

Industry/Entity Type

Clinical behaviour support and analysis

Colors
00AB8E
00BBA5
67D7C9
C6EFE9
E9F9F6

Requirements
Must have
• Soft colours, preferable pale turquoise, minimal pictures, clean, sophisticated and classical look

```html
<!DOCTYPE html>
<html lang="en">
<head>
<meta charset="utf-8">
<title>Calmora – Behaviour Support &amp; Analysis</title>
<link href="https://fonts.googleapis.com/css2?family=Montserrat:wght@500;600;700&family=Lato:wght@400;700&display=swap" rel="stylesheet">
<style>
:root{
  --teal:#00ab8e;
  --teal-2:#00bba5;
  --teal-3:#67d7c9;
  --mint:#c6efe9;
  --mint-pale:#e9f9f6;
  --topbar:#00ab8e;
  --ink:#1c2b36;
  --text:#5d6670;
  --line:#d8dde2;
  --frame:#dcf3ef;
  --white:#ffffff;
}
*{box-sizing:border-box;margin:0;padding:0}
html,body{width:1200px;height:2528px;overflow:hidden}
body{position:relative;background:var(--white);font-family:'Lato',sans-serif;color:var(--text)}
.abs{position:absolute}
.head{font-family:'Montserrat',sans-serif;color:var(--ink);font-weight:600}

.topbar{left:0;top:0;width:1200px;height:37px;background:var(--topbar);color:#e9f9f6;font-size:10px}
.topbar .welcome{left:225px;top:13px}
.topbar .contact-item{top:9px;display:flex;align-items:center;gap:8px;white-space:nowrap}
.dot{width:20px;height:20px;border-radius:50%;background:var(--teal-2);display:inline-flex;align-items:center;justify-content:center}
.topbar .dot{background:rgba(255,255,255,.25)}

.brand{display:flex;align-items:center;gap:8px;font-family:'Montserrat',sans-serif;font-weight:600;font-size:18px;color:var(--ink)}
.brand .mark{width:26px;height:26px;border-radius:50%;background:var(--teal)}
.nav{top:77px;font-family:'Montserrat',sans-serif;font-size:11px;color:var(--ink)}
.nav span{position:absolute;white-space:nowrap}
.nav .active{color:var(--teal)}
.navline{left:412px;top:126px;width:45px;height:2px;background:var(--teal)}
.btn-contact{left:885px;top:63px;width:90px;height:36px;background:var(--teal);color:#fff;font-family:'Montserrat',sans-serif;font-size:11px;display:flex;align-items:center;justify-content:center}

.hero{left:55px;top:128px;width:1090px;height:404px;background:linear-gradient(100deg,var(--mint),var(--mint-pale) 45%,#d6f2ed 80%,var(--mint-pale))}
.intro-title{left:0;width:1200px;top:594px;text-align:center;font-size:26px;line-height:29px;font-weight:700}
.intro-text{left:372px;width:456px;top:665px;text-align:center;font-size:9px;line-height:14.5px}
.video{left:225px;top:738px;width:750px;height:242px;background:linear-gradient(90deg,#e4ece9,#f2f6f4 40%,#dcebe7 70%,#eff5f3)}
.play{left:571px;top:830px;width:58px;height:58px;border-radius:50%;background:#fff;display:flex;align-items:center;justify-content:center}

.label{font-family:'Montserrat',sans-serif;font-size:9px;letter-spacing:3px;color:var(--ink);border:1px solid var(--line);padding:1px 4px}
.sec-title{font-size:19px;line-height:24px}
.para{font-size:9.5px;line-height:14.5px}
.bullets li{list-style:none;font-size:9.5px;margin-bottom:12px;position:relative;padding-left:10px}
.bullets li::before{content:"";position:absolute;left:0;top:5px;width:3px;height:3px;border-radius:50%;background:var(--ink)}

.band{left:0;top:1339px;width:1200px;height:313px;background:linear-gradient(135deg,var(--mint),var(--teal-3) 60%,#8fe0d5)}

.card{width:168px;height:205px;border:1px solid #e3efec;text-align:center}
.card .icon{position:absolute;left:45px;top:24px;width:78px;height:78px;border-radius:50%;background:var(--mint-pale);display:flex;align-items:center;justify-content:center}
.card h4{position:absolute;left:0;width:100%;top:118px;font-size:12.5px}
.card p{position:absolute;left:20px;width:128px;top:142px;font-size:9px;line-height:14.5px}

.footer{left:57px;top:2131px;width:1084px;height:351px;background:var(--mint-pale)}
.footer .col-title{font-family:'Montserrat',sans-serif;font-size:12.5px;font-weight:600;color:var(--ink)}
.footer ul li{list-style:none;font-size:9px;margin-bottom:9px}
.social{width:14px;height:14px;border-radius:50%;border:1.6px solid var(--teal)}
.copyright{left:0;width:1200px;top:2499px;text-align:center;font-size:9px}

.overlay{left:0;top:0;width:1200px;height:2528px;background:rgba(0,0,0,.66)}

.modal{left:238px;top:1216px;width:736px;height:552px;background:var(--frame)}
.modal .photo{position:absolute;left:12px;top:12px;width:288px;height:528px;background:linear-gradient(160deg,var(--mint),var(--mint-pale) 55%,#f7fbfa)}
.modal .panel{position:absolute;left:311px;top:12px;width:413px;height:528px;background:var(--white)}
.panel h2{position:absolute;left:44px;top:41px;font-size:25px;font-weight:700;white-space:nowrap}
.panel .lead{position:absolute;left:44px;top:88px;width:330px;font-size:9.5px;line-height:14.5px;color:#333}
.field{position:absolute;left:44px;width:331px;height:37px;border:1px solid var(--line);font-size:9.5px;color:#9aa2a9;padding:13px 0 0 19px}
.booking{position:absolute;left:44px;top:458px;width:331px;height:37px;background:var(--teal);color:#fff;font-size:10px;display:flex;align-items:center;justify-content:center}
</style>
</head>
<body>

<div class="abs topbar">
  <span class="abs welcome">Welcome to Calmora. We provide clinical behaviour support.</span>
  <span class="abs contact-item" style="left:731px"><span class="dot"><svg width="10" height="10" viewBox="0 0 24 24"><path fill="#fff" d="M6.6 10.8a15 15 0 0 0 6.6 6.6l2.2-2.2c.3-.3.7-.4 1-.2 1.1.4 2.3.6 3.6.6.6 0 1 .4 1 1V20c0 .6-.4 1-1 1A17 17 0 0 1 3 4c0-.6.4-1 1-1h3.5c.6 0 1 .4 1 1 0 1.3.2 2.5.6 3.6.1.3 0 .7-.2 1z"/></svg></span>(555) 210 - 4400</span>
  <span class="abs contact-item" style="left:867px"><span class="dot"><svg width="10" height="10" viewBox="0 0 24 24"><circle cx="12" cy="12" r="4" fill="none" stroke="#fff" stroke-width="2.5"/></svg></span>(555) 210 - 4400</span>
</div>

<div class="abs brand" style="left:225px;top:70px"><span class="mark"></span>Calmora</div>
<div class="abs nav" style="left:0;width:1200px;height:20px">
  <span class="active" style="left:419px">Home</span>
  <span style="left:479px">Services</span>
  <span style="left:544px">About</span>
  <span style="left:600px">Staff</span>
  <span style="left:650px">Referral</span>
  <span style="left:718px">Contacts</span>
</div>
<div class="abs navline"></div>
<svg class="abs" style="left:841px;top:76px" width="16" height="16" viewBox="0 0 24 24"><circle cx="10" cy="10" r="7" fill="none" stroke="#1c2b36" stroke-width="2"/><path d="M15 15l6 6" stroke="#1c2b36" stroke-width="2"/></svg>
<div class="abs btn-contact">Contact</div>

<div class="abs hero" role="img" aria-label="Calm photo of a clinician supporting a client"></div>

<h1 class="abs head intro-title">Our team helps you build<br>positive, lasting change.</h1>
<p class="abs intro-text">Our team of experienced clinicians uses evidence-based behaviour analysis to support people with a disability and the people around them. We carefully assess the reasons behind a behaviour and work with families, carers and providers on practical, respectful support.</p>

<div class="abs video" role="img" aria-label="Video still of a behaviour support session"></div>
<div class="abs play"><svg width="12" height="12" viewBox="0 0 10 10"><path d="M2 1l7 4-7 4z" fill="#1c2b36"/></svg></div>

<span class="abs label" style="left:225px;top:1052px">OUR STORY</span>
<h2 class="abs head sec-title" style="left:225px;top:1074px">Clinical behaviour<br>support &amp; analysis</h2>
<p class="abs para" style="left:225px;top:1133px;width:280px">We are a registered QCLP behaviour support practice, working with clients, families and support teams to understand behaviour.</p>
<p class="abs para" style="left:225px;top:1191px;width:280px">Every plan is built from a careful functional assessment and reviewed with the people who know the client best.</p>

<span class="abs label" style="left:613px;top:1050px">OUR MISSION</span>
<h2 class="abs head sec-title" style="left:613px;top:1073px">Our mission is to help clients<br>live better.</h2>
<p class="abs para" style="left:613px;top:1129px;width:300px">We reduce restrictive practices and build skills, so that each person can take part in daily life with more choice and confidence.</p>
<ul class="abs bullets" style="left:613px;top:1192px">
  <li>Registered QCLP behaviour support provider</li>
  <li style="margin-top:14px">Experienced, qualified behaviour clinicians</li>
</ul>

<div class="abs band" role="img" aria-label="Soft turquoise band with faint hexagon pattern"></div>

<h2 class="abs head" style="left:225px;top:1756px;font-size:25px;line-height:31px;font-weight:700">Our<br>services</h2>
<p class="abs para" style="left:638px;top:1797px">behaviour support tailored to each person.</p>

<div class="abs card" style="left:225px;top:1840px">
  <div class="icon"><svg width="26" height="26" viewBox="0 0 24 24"><circle cx="10" cy="10" r="6" fill="none" stroke="#00ab8e" stroke-width="2.4"/><path d="M14.5 14.5l6 6" stroke="#00ab8e" stroke-width="2.6"/></svg></div>
  <h4 class="head">Assessment</h4><p>Functional behaviour assessments that look at the causes of behaviour.</p>
</div>
<div class="abs card" style="left:421px;top:1840px">
  <div class="icon"><svg width="26" height="26" viewBox="0 0 24 24"><rect x="5" y="3" width="14" height="18" rx="2" fill="none" stroke="#00ab8e" stroke-width="2.2"/><path d="M8.5 12l2.5 2.5 4.5-5" stroke="#00ab8e" stroke-width="2.2" fill="none"/></svg></div>
  <h4 class="head">Support Plans</h4><p>Clear positive behaviour support plans written with the client.</p>
</div>
<div class="abs card" style="left:612px;top:1840px">
  <div class="icon"><svg width="26" height="26" viewBox="0 0 24 24"><path d="M3 9h4l10-5v16L7 15H3z" fill="#00ab8e"/><path d="M7 15l2 5h3l-2-5" fill="#00ab8e"/></svg></div>
  <h4 class="head">Carer Training</h4><p>Practical training for families, carers and support workers.</p>
</div>
<div class="abs card" style="left:806px;top:1840px">
  <div class="icon"><svg width="26" height="26" viewBox="0 0 24 24"><rect x="3" y="7" width="18" height="13" rx="2" fill="#00ab8e"/><path d="M9 7V4h6v3" stroke="#00ab8e" stroke-width="2" fill="none"/><path d="M12 10v7M8.5 13.5h7" stroke="#fff" stroke-width="2"/></svg></div>
  <h4 class="head">Expert Clinicians</h4><p>Qualified behaviour clinicians with years of disability experience.</p>
</div>

<div class="abs footer">
  <div class="abs brand" style="left:171px;top:67px"><span class="mark"></span>Calmora</div>
  <span class="abs" style="left:504px;top:71px;display:flex;align-items:center;gap:7px;font-size:9px;white-space:nowrap"><span class="dot" style="width:26px;height:26px;background:var(--teal)"><svg width="11" height="11" viewBox="0 0 24 24"><path fill="#fff" d="M6.6 10.8a15 15 0 0 0 6.6 6.6l2.2-2.2c.3-.3.7-.4 1-.2 1.1.4 2.3.6 3.6.6.6 0 1 .4 1 1V20c0 .6-.4 1-1 1A17 17 0 0 1 3 4c0-.6.4-1 1-1h3.5c.6 0 1 .4 1 1 0 1.3.2 2.5.6 3.6.1.3 0 .7-.2 1z"/></svg></span>(+00) 555 - 0142 - 300</span>
  <span class="abs" style="left:666px;top:71px;display:flex;align-items:center;gap:7px;font-size:9px;white-space:nowrap"><span class="dot" style="width:26px;height:26px;background:var(--teal)"><svg width="11" height="11" viewBox="0 0 24 24"><rect x="3" y="6" width="18" height="12" fill="none" stroke="#fff" stroke-width="2"/><path d="M3 6l9 7 9-7" fill="none" stroke="#fff" stroke-width="2"/></svg></span>hello@calmora-care.test</span>
  <span class="abs social" style="left:843px;top:78px"></span>
  <span class="abs social" style="left:874px;top:78px"></span>
  <span class="abs social" style="left:905px;top:78px"></span>

  <p class="abs head" style="left:168px;top:140px;width:230px;font-size:18px;line-height:26px;font-weight:600">“A Simple Story About The Calmora Behaviour Practice &amp; Support Team</p>

  <span class="abs col-title" style="left:448px;top:143px">Explore</span>
  <ul class="abs" style="left:448px;top:169px"><li>Home</li><li>Services</li><li>About us</li><li>Our Staff</li><li>Referral</li></ul>

  <span class="abs col-title" style="left:568px;top:143px">Useful Pages</span>
  <ul class="abs" style="left:568px;top:169px"><li>Referral Form</li><li>Resources</li><li>Privacy</li><li>Feedback</li><li>Contact</li></ul>

  <span class="abs col-title" style="left:715px;top:143px">Book an appointment</span>
  <p class="abs" style="left:715px;top:169px;width:200px;font-size:9px;line-height:14.5px">Leave your email and our intake team will contact you</p>
  <div class="abs" style="left:715px;top:205px;width:210px;height:36px;background:#fff;font-size:9px;color:#9aa2a9;padding:13px 0 0 15px">your email address</div>
  <div class="abs" style="left:715px;top:253px;width:90px;height:37px;background:var(--teal);color:#fff;font-size:10px;display:flex;align-items:center;justify-content:center">Submit</div>
</div>
<p class="abs copyright">Copyright © Calmora | Designed by Calmora Studio</p>

<div class="abs overlay"></div>

<div class="abs modal">
  <div class="photo" role="img" aria-label="Photo of a clinician taking notes in a consulting room"></div>
  <div class="panel">
    <h2 class="head">Book an appointment</h2>
    <p class="lead">Tell us a little about the support you need and our clinical team will be in touch to arrange a first visit.</p>
    <div class="field" style="top:135px">Name</div>
    <div class="field" style="top:185px">Email</div>
    <div class="field" style="top:235px">Phone</div>
    <div class="field" style="top:285px">Subject</div>
    <div class="field" style="top:335px;height:112px">Message...</div>
    <div class="booking">Booking Now</div>
  </div>
</div>

</body>
</html>
```